Irrigation Business needs their business cards modernised and revamped

I would like to keep my current logo, colours and revamp the format of the card.

I would like the card to be clean yet important.

Im not sure if you include texture but i would like the named logo to be indented into the card etc.

show me something alive and free something thats clinical to the point yet has a feel of achievement. i would like people to go nice card.

Target Market(s)

high end clients, corporate, sports field manger, the guys that make the decisions

Industry/Entity Type

Business

Contact Information for Business Card

nformation to be included

Gareth Minchin (Director)
0472958316
gareth@tkwater.biz
www.tomskerrywatering.com

instagram logo
google logo
facebook logo

Colors

Designer to choose colors to be used in the design.

Requirements
Nice to have
• indentations a really nice feel to the card good texture

```html
<!DOCTYPE html>
<html lang="en">
<head>
<meta charset="utf-8">
<title>Tom's Kerry Watering — Business Card</title>
<link rel="stylesheet" href="https://fonts.googleapis.com/css2?family=Arimo:wght@700&family=Open+Sans:wght@400&display=swap">
<style>
  :root {
    --page: #e8e4de;
    --card: #ffffff;
    --deep-blue: #3367ab;
    --sky-blue: #37a8d8;
    --leaf-green: #2e9c57;
    --white: #ffffff;
  }
  * { margin: 0; padding: 0; box-sizing: border-box; }
  html, body { width: 900px; height: 1200px; overflow: hidden; }
  body { background: var(--page); position: relative; font-family: "Arimo", Arial, sans-serif; }

  .card {
    position: absolute;
    width: 733px;
    height: 430px;
    background: var(--card);
    border-radius: 24px;
    overflow: hidden;
    box-shadow: 0 6px 14px rgba(0,0,0,0.18);
  }
  .card--front { left: 85px; top: 140px; }
  .card--back { left: 79px; top: 637px; }

  .wave { position: absolute; left: 0; top: 0; width: 733px; height: 430px; }
  .wave .band-deep { fill: var(--deep-blue); }
  .wave .band-sky { fill: var(--sky-blue); }

  .brand { position: absolute; text-align: center; color: var(--deep-blue); font-weight: 700; line-height: 1; }
  .brand__dot { display: block; margin: 0 auto; border-radius: 50%; border: 4px solid var(--deep-blue); }
  .brand__name { display: block; letter-spacing: -0.5px; }

  .card--front .brand { left: 60px; width: 320px; top: 34px; }
  .card--front .brand__dot { width: 124px; height: 124px; margin-bottom: 22px; }
  .card--front .brand__name { font-size: 36px; margin-top: 2px; }

  .card--back .brand { left: 166px; width: 400px; top: 87px; }
  .card--back .brand__dot { width: 132px; height: 132px; margin-bottom: 20px; }
  .card--back .brand__name { font-size: 40px; margin-top: 2px; }

  .holder { position: absolute; right: 48px; top: 48px; text-align: right; }
  .holder__name { font-size: 27px; color: var(--deep-blue); letter-spacing: 0.3px; }
  .holder__role { font-size: 18px; color: var(--leaf-green); margin-top: 6px; }

  .contact { position: absolute; right: 48px; top: 313px; list-style: none; font-family: "Open Sans", Arial, sans-serif; color: var(--white); font-size: 18px; }
  .contact li { display: flex; justify-content: flex-end; align-items: center; height: 28.5px; }
  .contact svg { width: 20px; height: 18px; margin-left: 10px; }

  .social { position: absolute; left: 48px; top: 366px; display: flex; gap: 12px; }
  .social span { width: 31px; height: 31px; border-radius: 50%; background: var(--white); border: 3px solid #7fc6e6; }
</style>
</head>
<body>

<section class="card card--front">
  <svg class="wave" viewBox="0 0 733 430" aria-hidden="true">
    <path class="band-deep" d="M0,255 C120,290 260,308 380,298 C500,285 620,212 733,196 L733,220 C620,232 500,292 380,306 C250,318 120,302 0,286 Z"/>
    <path class="band-sky" d="M0,292 C140,312 280,322 400,312 C520,298 630,242 733,228 L733,248 C630,260 520,308 400,322 C270,334 130,328 0,318 Z"/>
    <path class="band-deep" d="M0,326 C150,346 300,342 420,324 C540,304 640,264 733,255 L733,430 L0,430 Z"/>
  </svg>

  <div class="brand">
    <span class="brand__dot"></span>
    <span class="brand__name">TOM'S KERRY</span>
    <span class="brand__name">WATERING</span>
  </div>

  <div class="holder">
    <div class="holder__name">GARETH MINCHIN</div>
    <div class="holder__role">DIRECTOR</div>
  </div>

  <ul class="contact">
    <li>0472958316
      <svg viewBox="0 0 20 18" aria-label="phone"><path fill="#fff" d="M2,5 C2,2 6,1 10,1 C14,1 18,2 18,5 L14,6 L13,4 C11,3.5 9,3.5 7,4 L6,6 Z M5,8 L15,8 L17,16 L3,16 Z"/><circle cx="10" cy="12" r="2.2" fill="#3367ab"/></svg>
    </li>
    <li>gareth@tkwater.biz
      <svg viewBox="0 0 20 18" aria-label="email"><rect x="1" y="3" width="18" height="12" fill="#fff"/><path d="M1,3 L10,10 L19,3 M1,15 L8,8.5 M19,15 L12,8.5" stroke="#3367ab" stroke-width="1.2" fill="none"/></svg>
    </li>
    <li>www.tomskerrywatering.com
      <svg viewBox="0 0 20 18" aria-label="website"><circle cx="10" cy="9" r="8" fill="#fff"/><path d="M6,5 C8,4 9,6 8,8 C6,9 5,7 6,5 Z M11,10 C14,9 15,12 13,14 C11,14 10,12 11,10 Z" fill="#3367ab"/></svg>
    </li>
  </ul>

  <div class="social" aria-label="social media">
    <span></span><span></span><span></span>
  </div>
</section>

<section class="card card--back">
  <svg class="wave" viewBox="0 0 733 430" aria-hidden="true">
    <g transform="translate(0,58)">
      <path class="band-deep" d="M0,255 C120,290 260,308 380,298 C500,285 620,212 733,196 L733,220 C620,232 500,292 380,306 C250,318 120,302 0,286 Z"/>
      <path class="band-sky" d="M0,292 C140,312 280,322 400,312 C520,298 630,242 733,228 L733,248 C630,260 520,308 400,322 C270,334 130,328 0,318 Z"/>
      <path class="band-deep" d="M0,326 C150,346 300,342 420,324 C540,304 640,264 733,255 L733,430 L0,430 Z"/>
    </g>
  </svg>

  <div class="brand">
    <span class="brand__dot"></span>
    <span class="brand__name">TOM'S KERRY</span>
    <span class="brand__name">WATERING</span>
  </div>
</section>

</body>
</html>
```